2018 Recital Flyer, "Beyond Every Wall" for Cobalt Step Academy

I have a Dance Studio, Cobalt Step Academy, LLC (CobaltStepRivera.example) and we are having a Dance Recital in June entitled, "Beyond Every Wall". The concept of the recital is about overcoming obstacles and pushing forward in spite of adversity...Triumph over Defeat... Victory, Achievement, Success, Conquest, Hero's, Standing Up for Something, Inspiring moments, girl power, etc...we will perform to music that has this type of message.

I would like a design that can capture this type of message, maybe some animated dancers leaping over a big rock or a mountain???? Not sure, but I am open to your artistic vision!

The text on the flyer should include:

Cobalt Step Academy, LLC
Presents
Our 7th Annual Recital, "Beyond Every Wall"
Saturday, June 23, 2018, 2 PM & 7 PM
Pinecrest Harbor Middle School
412 Mulvane Rd, Dorsey Township, MI 48217

I am looking forward to a great design
Thanks,
I have attached my logo for your review

Target Market(s)

Dance / Entertainment enthusiasts, Kids, Moms, concert goers...

Industry/Entity Type

Performing Art

Colors

Designer to choose colors to be used in the design.

Requirements
Must have
• all detailed information and logo on the design, something eye-catching and interesting
Nice to have
• ???

```html
<!DOCTYPE html>
<html lang="en">
<head>
<meta charset="utf-8">
<title>Beyond Every Wall – Cobalt Step Academy 7th Annual Recital</title>
<link rel="stylesheet" href="https://fonts.googleapis.com/css2?family=Roboto:ital,wght@0,300;0,400;0,500;1,700&family=Roboto+Condensed:wght@400&family=Great+Vibes&family=Special+Elite&family=Black+Ops+One&family=Kalam:wght@700&family=Playfair+Display:ital@0;1&display=swap">
<style>
  :root {
    --backdrop: #e9eaec;
    --paper: #ffffff;
    --art-dark: #4a2a24;
    --art-mid: #b45a3a;
    --art-orange: #e88a4a;
    --art-pink: #d76aa8;
    --art-violet: #9a4a9a;
    --photo-gold: #e9b46a;
    --photo-peach: #d98a6a;
    --photo-plum: #b4589c;
    --gold: #f4e400;
    --cream: #f3e6c4;
    --ink-dark: #3a2a22;
    --brand-red: #8e1f1f;
    --date-red: #b3262a;
    --text-black: #111111;
    --white: #ffffff;
  }
  * { margin: 0; padding: 0; box-sizing: border-box; }
  html, body { width: 1200px; height: 1200px; overflow: hidden; background: var(--backdrop); }
  .poster {
    position: absolute; left: 230px; top: 30px; width: 740px; height: 1140px;
    background: var(--paper); overflow: hidden;
    box-shadow: 0 6px 24px rgba(0,0,0,.18);
  }
  .poster__art { position: absolute; left: 0; top: 0; width: 740px; height: 900px; }
  .poster__photo { position: absolute; left: 0; top: 40px; width: 400px; height: 800px; }
  .header { position: absolute; left: 290px; width: 400px; text-align: center; white-space: nowrap; }
  .header__studio { top: 42px; font: 400 31px "Roboto Condensed", sans-serif; color: var(--gold); }
  .header__presents { top: 84px; font: 500 27px "Roboto", sans-serif; letter-spacing: 6px; color: var(--gold); }
  .header__recital { top: 122px; font: 400 38px "Great Vibes", cursive; color: var(--white); }
  .title { position: absolute; left: 310px; width: 400px; text-align: center; font-family: "Black Ops One", sans-serif; color: var(--cream); text-shadow: 2px 3px 0 rgba(60,25,15,.55); line-height: 1; white-space: nowrap; }
  .title__line--1 { top: 186px; font-size: 78px; }
  .title__line--2 { top: 284px; font-size: 66px; }
  .title__line--3 { top: 362px; font-size: 88px; }
  .tagline { position: absolute; left: 340px; width: 330px; top: 462px; text-align: center; font: italic 400 18px/22px "Playfair Display", serif; color: var(--ink-dark); text-transform: uppercase; }
  .tagline__low { text-transform: none; }
  .words { position: absolute; left: 340px; width: 330px; text-align: center; line-height: 1; white-space: nowrap; }
  .words--1 { top: 536px; font: 700 22px "Kalam", cursive; color: var(--white); }
  .words--2 { top: 566px; color: var(--ink-dark); }
  .words--3 { top: 596px; color: var(--text-black); }
  .script { font: 400 24px "Great Vibes", cursive; }
  .caps { font: 700 22px "Kalam", cursive; color: var(--white); }
  .typed { font: 400 26px "Special Elite", monospace; }
  .bold-it { font: italic 700 26px "Roboto", sans-serif; }
  .brand { position: absolute; left: 30px; top: 1000px; width: 330px; display: flex; align-items: center; justify-content: center; gap: 10px; }
  .brand__mark { width: 22px; height: 22px; border-radius: 50%; background: var(--brand-red); flex: none; }
  .brand__name { font: 500 24px "Roboto", sans-serif; color: var(--brand-red); white-space: nowrap; }
  .divider { position: absolute; left: 377px; top: 958px; width: 1px; height: 130px; background: var(--ink-dark); }
  .event { position: absolute; left: 390px; width: 340px; top: 962px; text-align: center; }
  .event__day { font: italic 700 25px "Roboto", sans-serif; color: var(--brand-red); }
  .event__date { font: 300 23px "Roboto", sans-serif; color: var(--date-red); margin-top: 2px; white-space: nowrap; }
  .event__venue { font: 500 15px/19px "Roboto", sans-serif; color: var(--text-black); margin-top: 2px; }
</style>
</head>
<body>
<main class="poster">
  <svg class="poster__art" viewBox="0 0 740 900" aria-hidden="true">
    <defs>
      <linearGradient id="artFill" x1="0" y1="0" x2="0.6" y2="1">
        <stop offset="0" stop-color="var(--art-dark)"/>
        <stop offset="0.35" stop-color="var(--art-mid)"/>
        <stop offset="0.6" stop-color="var(--art-orange)"/>
        <stop offset="0.85" stop-color="var(--art-pink)"/>
        <stop offset="1" stop-color="var(--art-violet)"/>
      </linearGradient>
    </defs>
    <path fill="url(#artFill)" d="M0 0 H740 V470 C725 520 700 560 650 600 C640 640 600 700 520 760 C470 800 400 800 330 820 C270 840 180 860 120 870 C70 880 30 860 0 840 Z"/>
  </svg>

  <svg class="poster__photo" viewBox="0 0 400 800" role="img" aria-label="Photo of a leaping dancer in a green crop top and denim shorts, arms raised, in front of a large golden marquee-light star">
    <defs>
      <linearGradient id="photoFill" x1="0" y1="0" x2="0.3" y2="1">
        <stop offset="0" stop-color="var(--photo-peach)" stop-opacity="0.55"/>
        <stop offset="0.55" stop-color="var(--photo-gold)" stop-opacity="0.85"/>
        <stop offset="1" stop-color="var(--photo-plum)" stop-opacity="0.9"/>
      </linearGradient>
    </defs>
    <path fill="url(#photoFill)" d="M40 20 C120 0 260 60 320 200 C360 300 390 450 380 600 C372 700 300 770 200 790 C120 800 40 780 0 740 V60 Z"/>
  </svg>

  <div class="header header__studio">Cobalt Step Academy, LLC</div>
  <div class="header header__presents">PRESENTS</div>
  <div class="header header__recital">7th Annual Recital</div>

  <h1>
    <span class="title title__line--1">BEYOND</span>
    <span class="title title__line--2">EVERY</span>
    <span class="title title__line--3">WALL</span>
  </h1>

  <p class="tagline">Overcoming obstacles<br>and pushing forward in<br>spite of <span class="tagline__low">adversity</span></p>
  <p class="words words--1">Triumph over Defeat</p>
  <p class="words words--2"><span class="script">Achievement</span> <span class="caps">VICTORY</span></p>
  <p class="words words--3"><span class="bold-it">SUCCESS</span> <span class="typed">Conquest</span></p>

  <div class="brand">
    <span class="brand__mark"></span>
    <span class="brand__name">Cobalt Step Academy, LLC</span>
  </div>

  <div class="divider"></div>

  <section class="event">
    <p class="event__day">SATURDAY,</p>
    <p class="event__date">JUNE 23, 2018, 2 PM &amp; 7 PM</p>
    <p class="event__venue">Pinecrest Harbor Middle School<br>412 Mulvane Rd, Dorsey Township,<br>MI 48217</p>
  </section>
</main>
</body>
</html>
```